Flyer für Wasser-, Brand- und Schimmelschadensanierung
Zielgruppe
Wir sind spezialisiert im Bereich Wasser-, Brand- und Schimmelschadensanierung
Aufgabenstellung
Folgende Design Anforderungen
Durchgehend ein professionelles, ruhiges Farbschema (z.B. Blau-Töne für Vertrauen, kombiniert mit Grau/Weiß).
· Konsistente Nutzung von Icons für bessere visuelle Führung.
· Whitespace, um Lesbarkeit zu erhöhen.
· Hochwertige, authentische Fotos aus echten Projekten (vorher/nachher Bilder sind sehr wirksam).
Folgender Inhalt:
Seite 1 (Titelseite / Eyecatcher)
· Logo & Claim: Großzügige Platzierung des Logos KLT-RENOVATIO. Darunter ein prägnanter Claim, z.B.:
· 'Ihr zuverlässiger Partner bei Wasser-, Brand- und Schimmelschäden.'
· Oder: 'Volle Restitution. Reibungslose Regulierung.'
· Visuell: Hochwertiges, emotionsgeladenes Bild, das Kompetenz und Zuversicht vermittelt (z.B. ein zufriedener Kunde mit unserem Team im sanierten Raum, oder ein fokussierter Techniker bei der Arbeit mit modernem Gerät).
· Kontaktdaten (unten, klar lesbar):
· Webseite: www.KLT-Renovatio.de
· Telefon: 0800 - [Ihre Nummer] (24/7 Notdienst)
· E-Mail: info@klt-renovatio.de
Seite 2 & 3 (Innenseiten beim Aufklappen – das Herzstück)
Überschrift: Unsere Philosophie & Ihr Vorteil
· Ein kurzer, einleitender Text (ca. 4-5 Zeilen):
'Ein Schaden bedeutet Stress und Unsicherheit. Als Ihr spezialisierter Dienstleister übernehmen wir die komplette Koordination – von der ersten Sofortmaßnahme bis zur schlüsselfertigen Wiederherstellung. Wir entlasten Geschädigte und bieten unseren Partnern aus der Versicherungswirtschaft einen effizienten, dokumentierten und kostentransparenten Prozess. Weil Sie sich auf Experten verlassen können.'
Aufbau in zwei Spalten:
Linke Spalte: FÜR GESCHÄDIGTE & EIGENTÜMER
· Sub-Überschrift: Ihre Sicherheit in der Schadenssituation
· Kernleistungen als leicht verständliche Icons/Stichpunkte:
· Soforthilfe 24/7: Wir kommen schnell und stoppen den Schaden.

```html
<!DOCTYPE html>
<html lang="de">
<head>
<meta charset="utf-8">
<title>KLT Renovatio – Flyer Titelseite</title>
<link href="https://fonts.googleapis.com/css2?family=Open+Sans:wght@400;600;700;800&display=swap" rel="stylesheet">
<style>
  :root {
    --navy: #1c1f4e;
    --blue: #1a78c2;
    --orange: #ef8a2e;
    --white: #ffffff;
    --ink: #1c1f4e;
    --wall-light: #f3eee6;
    --wall-mid: #ddd3c5;
    --wall-shade: #b9ab98;
    --shirt-blue: #3f6499;
    --shirt-deep: #23406f;
  }
  * { margin: 0; padding: 0; box-sizing: border-box; }
  html, body { width: 847px; height: 1200px; overflow: hidden; background: var(--white); }
  body { font-family: "Open Sans", Arial, sans-serif; }
  .flyer { position: relative; width: 847px; height: 1200px; overflow: hidden; background: var(--white); }
  .top-bar { position: absolute; top: 0; left: 0; width: 100%; height: 12px; background: var(--navy); }

  .brand { position: absolute; top: 48px; left: 60px; }
  .brand-row { display: flex; align-items: center; gap: 16px; }
  .brand-mark { width: 58px; height: 58px; border-radius: 50%; background: var(--blue); flex: none; }
  .brand-name { font-weight: 700; font-size: 34px; line-height: 1.05; color: var(--ink); }
  .brand-tagline { margin-top: 14px; font-size: 15px; font-weight: 600; color: var(--ink); }

  .claim { position: absolute; left: 40px; top: 331px; z-index: 2; }
  .claim-line { display: block; width: max-content; color: var(--white); font-weight: 700; font-size: 44px; line-height: 1; padding: 10px 21px 10px; }
  .claim-line--first { background: var(--orange); }
  .claim-line--second { background: var(--blue); margin-left: 29px; margin-top: 4px; }

  .art { position: absolute; left: 0; top: 0; width: 847px; height: 1200px; }

  .contact { position: absolute; right: 52px; top: 1052px; text-align: right; color: var(--white); font-size: 24px; line-height: 33px; font-weight: 400; font-style: normal; }
</style>
</head>
<body>
<div class="flyer">
  <div class="top-bar"></div>

  <svg class="art" viewBox="0 0 847 1200">
    <defs>
      <linearGradient id="photoTone" x1="0.1" y1="0.1" x2="0.9" y2="0.85">
        <stop offset="0" stop-color="var(--wall-light)"/>
        <stop offset="0.35" stop-color="var(--wall-mid)"/>
        <stop offset="0.55" stop-color="var(--wall-shade)"/>
        <stop offset="0.75" stop-color="var(--shirt-blue)"/>
        <stop offset="1" stop-color="var(--shirt-deep)"/>
      </linearGradient>
    </defs>
    <circle cx="660" cy="830" r="400" fill="none" stroke="var(--orange)" stroke-width="2"/>
    <circle cx="660" cy="830" r="385" fill="none" stroke="var(--orange)" stroke-width="2"/>
    <circle cx="660" cy="830" r="365" fill="url(#photoTone)" role="img" aria-label="Foto: Handwerker in blauem Hemd restauriert eine Stuckverzierung an einer hellen Zimmerdecke"/>
    <path d="M0 985 C 150 945, 260 955, 380 975 C 520 1000, 640 960, 847 930 L 847 1200 L 0 1200 Z" fill="var(--navy)"/>
  </svg>

  <header class="brand">
    <div class="brand-row">
      <span class="brand-mark"></span>
      <span class="brand-name">KLT<br>Renovatio</span>
    </div>
    <p class="brand-tagline">Wasser • Brand • Schimmelschäden</p>
  </header>

  <div class="claim">
    <span class="claim-line claim-line--first">Volle Restitution.</span>
    <span class="claim-line claim-line--second">Reibungslose Regulierung.</span>
  </div>

  <address class="contact">
    Webseite: www.KLT-Renovatio.de<br>
    Telefon: 0800 - [12345] (24/7 Notdienst)<br>
    E-Mail: info@klt-renovatio.de
  </address>
</div>
</body>
</html>
```